Etiketten für Honig
Zielgruppe
Bienenhaus Amboss / Verkauf von Honig - eigene Völker ( Produktion)
Zielgruppe: Privatpersonen (Freunde, Bekannte) keine Zwischenhändler
Aufgabenstellung
Ich wohne in einem alten Fachwerkhaus, welches ursprünglich als Schmiede gebaut wurde.
Honig& Schmiede oder Biene & Schmiede sollten berücksichtigt werden
Stichwort: Schmiedehonig oder so ähnlich
Etiketten mit Verbraucherschutz
Ursprung Deutschland
Gläser: Neutral
Abmessungen:
•Durchmesser: 8,05 cm
•Gesamthöhe: 9,4 cm
•Höhe ohne Gewinde: 8,05 cm

```html
<!DOCTYPE html>
<html lang="de">
<head>
<meta charset="utf-8">
<title>Waldhonig – Etiketten</title>
<link rel="stylesheet" href="https://fonts.googleapis.com/css2?family=Questrial&family=Roboto+Condensed:wght@400;700&display=swap">
<style>
  :root {
    --canvas: #ebebeb;
    --ink-dark: #232323;
    --gold: #b8902f;
    --white: #ffffff;
    --text-light: #ececec;
    --comb-red: #b8451c;
    --comb-amber: #d9822f;
    --comb-violet: #8a7aa8;
    --fire-dark: #1c1410;
    --fire-orange: #e5641f;
    --fire-yellow: #f6c04a;
  }
  * { margin: 0; padding: 0; box-sizing: border-box; }
  html, body { width: 1200px; height: 1200px; overflow: hidden; }
  body { background: var(--canvas); position: relative; font-family: "Roboto Condensed", sans-serif; }

  /* Markenkachel */
  .brand-tile {
    position: absolute; left: 50px; top: 165px; width: 220px; height: 220px;
    background: var(--ink-dark);
    display: flex; flex-direction: column; align-items: center; justify-content: center; gap: 14px;
  }
  .brand-dot { width: 12px; height: 12px; border-radius: 50%; background: var(--gold); }
  .brand-name {
    font-family: "Questrial", sans-serif; color: var(--gold);
    text-transform: uppercase; text-align: center;
  }
  .brand-tile .brand-name { font-size: 22px; letter-spacing: 3px; line-height: 1.4; }

  /* Etiketten */
  .label {
    position: absolute; left: 300px; width: 860px; height: 415px;
    background: var(--ink-dark); overflow: hidden; color: var(--white);
  }
  .label--band { top: 165px; }
  .label--full { top: 620px; }

  .photo-comb, .photo-fire { position: absolute; top: 0; width: 430px; }
  .photo-comb {
    left: 0;
    background: linear-gradient(120deg, var(--comb-red) 0%, var(--comb-amber) 35%, var(--comb-violet) 70%, var(--comb-amber) 100%);
  }
  .photo-fire {
    left: 430px;
    background: radial-gradient(ellipse at 50% 75%, var(--fire-yellow) 0%, var(--fire-orange) 25%, #6a2a10 52%, var(--fire-dark) 78%);
  }
  .label--band .photo-comb, .label--band .photo-fire { height: 240px; }
  .label--full .photo-comb, .label--full .photo-fire { height: 415px; }

  .weight {
    position: absolute; right: 30px; top: 24px;
    color: var(--gold); font-weight: 700; font-size: 20px;
  }
  .title {
    position: absolute; left: 0; width: 860px; text-align: center;
    font-family: "Questrial", sans-serif; font-weight: 400; font-size: 82px; line-height: 1;
    color: var(--white); letter-spacing: -1px;
  }
  .label--band .title { top: 82px; }
  .label--full .title { top: 42px; }

  .subtitle-bar {
    position: absolute; left: 258px; top: 128px; width: 344px; height: 28px;
    background: var(--ink-dark); color: #d6d6d6;
    font-family: "Questrial", sans-serif; font-size: 18px; letter-spacing: 1.5px;
    text-align: center; line-height: 28px; text-transform: uppercase;
  }

  .address {
    position: absolute; left: 30px; font-size: 18px; line-height: 21px; color: var(--text-light);
  }
  .address strong { font-weight: 700; color: var(--white); }
  .label--band .address { top: 282px; }
  .address-box {
    position: absolute; left: 0; bottom: 0; width: 226px; height: 160px; background: var(--ink-dark);
  }
  .label--full .address { top: 272px; }

  .storage {
    position: absolute; right: 30px; text-align: right; font-size: 18px; line-height: 21px; color: var(--text-light);
  }
  .storage .best-before { display: block; margin-top: 14px; font-size: 16px; }
  .label--band .storage { top: 282px; }
  .label--full .storage { top: 266px; }

  .band-mark {
    position: absolute; left: 330px; top: 258px; width: 200px; height: 130px;
    display: flex; align-items: center; justify-content: center;
  }
  .band-mark .brand-name { font-size: 22px; letter-spacing: 2.5px; line-height: 1.4; }
</style>
</head>
<body>

  <div class="brand-tile">
    <span class="brand-dot"></span>
    <span class="brand-name">Bienenhaus<br>Amboss</span>
  </div>

  <section class="label label--band">
    <div class="photo-comb" role="img" aria-label="Nahaufnahme einer Honigwabe in Rot, Bernstein und Violett"></div>
    <div class="photo-fire" role="img" aria-label="Glühendes Schmiedefeuer mit Flammen in dunkler Esse"></div>
    <span class="weight">500g</span>
    <h1 class="title">Waldhonig</h1>
    <p class="address">Bienenhaus Amboss<br>Musterstraße 1<br>12345 Musterstadt<br>Tel: 0123 /456<br><strong>www.bienenhaus-amboss.de</strong></p>
    <div class="band-mark"><span class="brand-name">Bienenhaus<br>Amboss</span></div>
    <p class="storage">Trocken und vor Wärme<br>geschützt lagern!<span class="best-before">Mindesten haltbar bis:</span></p>
  </section>

  <section class="label label--full">
    <div class="photo-comb" role="img" aria-label="Nahaufnahme einer Honigwabe in Rot, Bernstein und Violett"></div>
    <div class="photo-fire" role="img" aria-label="Glühendes Werkstück im Schmiedefeuer"></div>
    <span class="weight">500g</span>
    <h2 class="title">Waldhonig</h2>
    <div class="subtitle-bar">Bienenhaus-Amboss</div>
    <div class="address-box"></div>
    <p class="address">Bienenhaus Amboss<br>Musterstraße 1<br>12345 Musterstadt<br>Tel: 0123 /456<br><strong>www.bienenhaus-amboss.de</strong></p>
    <p class="storage">Trocken und vor Wärme<br>geschützt lagern!<span class="best-before">Mindesten haltbar bis:</span></p>
  </section>

</body>
</html>
```